Vindmark Health & Wellness needs a fresh and interesting website

I need a rebrand and redevelopment of my website, www.dellaquorne.example
Our mission is provide bespoke , lifestyle medicine , everyone has their own path to health. and we are creating a personalized experience for people to life their life to the fullest
Vindmark - means sea lands
I need an landing page and about page and potentially a few project launch pages , I have been using Wordpress for my basic information and then I use Plovix for the launch pages of my programs since I can edit those easily.

Target Market(s)

Corporate and individual's who are interested in a different perspective on health and wellness , and living with a chronic illness

Industry/Entity Type

Health, lifestyle , wellness coaching and medicine

Coding

Number of Pages Required

Font styles to use
Other font styles liked:
• look into the logo

Requirements
Must have
• the logo I uploaded
Nice to have
• I want a fresh perspective on health, I have bamboo, hibiscus vibes in my logo , but also like more of a water vibe/ I want something earthy but not too boho it needs to be clean
Should not have
• every other holistic health vibe,

```html
<!DOCTYPE html>
<html lang="en">
<head>
<meta charset="utf-8">
<title>Vindmark Health &amp; Wellness</title>
<link href="https://fonts.googleapis.com/css2?family=Noto+Serif:ital,wght@0,300;0,400;1,300&family=Montserrat:wght@400;500;600;700&family=Great+Vibes&display=swap" rel="stylesheet">
<style>
:root{
  --green:#3f5634;
  --green-dark:#35492c;
  --lime:#93bd55;
  --lime-strip:#b1d483;
  --teal:#1f6f8e;
  --bg:#eef4f5;
  --ink:#1d1d1d;
  --muted:#555b5c;
  --white:#ffffff;
  --black:#111213;
  --serif:'Noto Serif',Georgia,serif;
  --sans:'Montserrat',Arial,sans-serif;
}
*{margin:0;padding:0;box-sizing:border-box}
html,body{width:1200px;height:4082px;overflow:hidden}
body{background:var(--bg);font-family:var(--sans);color:var(--ink);position:relative}
section,header,footer{position:absolute;left:0;width:1200px}
.abs{position:absolute}
.label{font-family:var(--sans);font-size:8px;letter-spacing:2px;font-weight:600;color:var(--lime);text-transform:uppercase;display:flex;align-items:center;gap:10px}
.label .rule{display:inline-block;width:36px;height:1px;background:var(--lime)}
.title{font-family:var(--serif);font-weight:300;text-transform:uppercase;color:var(--ink);line-height:1.15}

/* header */
.site-header{top:0;height:83px;background:var(--white)}
.nav a{position:absolute;top:38px;font-size:10.5px;color:var(--ink);text-decoration:none;font-weight:500;text-transform:uppercase}
.nav a.active:after{content:"";position:absolute;left:0;right:0;bottom:-8px;height:1px;background:var(--ink)}
.brand{position:absolute;left:540px;top:14px;width:120px;text-align:center;font-family:var(--serif);color:var(--teal);font-size:20px;font-weight:400;line-height:1.1}
.brand .dot{display:block;width:18px;height:18px;border-radius:50%;background:var(--teal);margin:0 auto 4px}
.btn-outline{position:absolute;border:1.5px solid var(--teal);border-radius:30px;font-size:8px;letter-spacing:2px;font-weight:600;color:var(--teal);display:flex;align-items:center;justify-content:center;text-transform:uppercase}

/* hero */
.hero{top:83px;height:434px;background:var(--green)}
.hero-photo{left:0;top:0;width:664px;height:434px;background:linear-gradient(160deg,#d9d3c0 0%,#a79c80 35%,#6f7a74 60%,#3b3f3a 100%)}
.hero-copy{left:745px;top:88px;width:330px;color:var(--white)}
.hero-copy .eyebrow{font-size:8px;letter-spacing:2px;font-weight:600}
.hero-copy h1{font-family:var(--serif);font-weight:300;font-size:41px;line-height:1.17;margin-top:14px;letter-spacing:.5px}
.hero-copy .bar{width:20px;height:2px;background:var(--white);margin:12px 0 14px}
.hero-copy p{font-size:10.5px;line-height:1.6}
.arrow-pair{display:flex}
.arrow-pair span{width:44px;height:44px;border-radius:50%;display:flex;align-items:center;justify-content:center}
.arrow-pair .dark{background:var(--green-dark)}
.arrow-pair .soft{background:#6a7d5c;margin-left:-4px}

/* about */
.about{top:517px;height:616px}
.photo{border-radius:8px}
.photo-frame{border:5px solid var(--white);border-radius:10px}
.about p{font-size:10.5px;line-height:1.62;color:var(--muted)}
.signature{font-family:'Great Vibes',cursive;font-size:30px;color:var(--ink)}

/* quote */
.quote{top:1133px;height:470px;background:linear-gradient(180deg,#3a4340 0%,#2b3330 45%,#1f2a22 100%)}
.quote blockquote{position:absolute;left:330px;width:540px;top:96px;text-align:center;font-family:var(--serif);font-style:italic;font-weight:300;font-size:28px;line-height:1.2;color:var(--white)}

/* offerings */
.offerings{top:1603px;height:827px}
.mountains{left:0;top:500px;width:1200px;height:327px;background:linear-gradient(180deg,var(--bg) 0%,#c9dde0 35%,#a66a4c 75%,#4f3a33 100%)}
.card{position:absolute;top:215px;width:301px}
.card .img{height:162px;border-radius:6px}
.card .meta{font-size:9px;color:var(--ink);margin:18px 6px 0;display:flex;gap:12px;align-items:center}
.card .excerpt{font-size:10.5px;line-height:1.38;font-weight:500;margin:6px 6px 0}
.card .line{height:1px;background:#d2d7d8;margin:12px 6px 0}
.card .more{font-size:8px;letter-spacing:2px;font-weight:700;margin:16px 6px 0}

/* kind words */
.kind{top:2430px;height:488px}
.kind p{font-size:10px;line-height:1.65;color:var(--muted)}

/* reviews */
.reviews{top:2918px;height:407px;background:var(--green)}
.reviews .strip{left:0;top:0;width:85px;height:407px;background:var(--lime-strip)}
.review{position:absolute;background:var(--white);border-radius:12px;padding:26px 38px}
.stars{color:#c5b400;font-size:10px;letter-spacing:1px}
.review .text{font-family:var(--serif);font-size:15px;line-height:1.4;color:var(--ink);margin-top:10px}
.review .rule{width:30px;height:1px;background:#999;margin:14px 0 10px}
.review .name{font-size:13px;color:var(--ink);font-weight:500}

/* cta */
.cta{top:3325px;height:513px;text-align:center}

/* footer */
.site-footer{top:3838px;height:244px;background:var(--black);color:var(--white)}
.footer-brand{left:132px;top:60px;width:150px;text-align:center;font-family:var(--serif);font-size:26px;line-height:1}
.footer-brand .dot{display:block;width:30px;height:30px;border-radius:50%;background:var(--white);margin:0 auto 8px}
.footer-nav a{position:absolute;top:131px;font-size:9.5px;color:var(--white);text-decoration:none;text-transform:uppercase;font-weight:500}
.social span{position:absolute;top:124px;width:24px;height:24px;border-radius:50%;border:1px solid #555;background:#222}
.fine{position:absolute;top:203px;font-family:var(--serif);font-size:8.5px;color:var(--white)}
</style>
</head>
<body>

<header class="site-header">
  <nav class="nav">
    <a class="active" style="left:148px">Home</a>
    <a style="left:208px">About Us</a>
    <a style="left:293px">Services</a>
    <a style="left:373px">Corporate Wellness</a>
    <a style="left:712px">Wellness</a>
    <a style="left:806px">Events</a>
    <a style="left:876px">Blogs</a>
  </nav>
  <div class="brand"><span class="dot"></span>Vindmark</div>
  <div class="btn-outline" style="left:939px;top:26px;width:129px;height:31px">Contact Us</div>
</header>

<section class="hero">
  <div class="abs hero-photo" role="img" aria-label="Hand balancing a stack of stones by a sunlit lake with mountains"></div>
  <div class="abs hero-copy">
    <div class="eyebrow">WELCOME TO VINDMARK</div>
    <h1>PATH TO<br>PERSONALIZED<br>WELLNESS</h1>
    <div class="bar"></div>
    <p>We believe in the power of bespoke lifestyle medicine. We understand that everyone has their unique journey to health, and we're here to provide the personalized guidance and support you need to live life to the fullest.</p>
  </div>
  <div class="abs arrow-pair" style="left:620px;top:368px">
    <span class="dark"><svg width="10" height="10" viewBox="0 0 10 10"><path d="M6.5 1.5 3 5l3.5 3.5" fill="none" stroke="#fff" stroke-width="1.6"/></svg></span>
    <span class="soft"><svg width="10" height="10" viewBox="0 0 10 10"><path d="M3.5 1.5 7 5 3.5 8.5" fill="none" stroke="#fff" stroke-width="1.6"/></svg></span>
  </div>
</section>

<section class="about">
  <div class="abs photo" style="left:193px;top:97px;width:305px;height:270px;background:linear-gradient(180deg,#6f8b74 0%,#3f6a3a 55%,#4a3a2a 100%)" role="img" aria-label="Hands holding a young tree seedling in soil above a green valley"></div>
  <div class="abs photo-frame" style="left:388px;top:266px;width:232px;height:252px">
    <div style="width:100%;height:100%;border-radius:6px;background:linear-gradient(160deg,#e6e6e6 0%,#9a9a9a 50%,#3a3a3a 100%)" role="img" aria-label="Black and white portrait of the practitioner in a wide-brimmed hat"></div>
  </div>
  <svg class="abs" style="left:158px;top:383px" width="90" height="90" viewBox="0 0 90 90" role="img" aria-label="30 years of experience badge">
    <circle cx="45" cy="45" r="43" fill="var(--bg)"/>
    <circle cx="45" cy="45" r="12" fill="none" stroke="var(--teal)" stroke-width="1.5"/>
    <defs><path id="ring" d="M45 45 m-32 0 a32 32 0 1 1 64 0 a32 32 0 1 1 -64 0"/></defs>
    <text font-family="Montserrat,sans-serif" font-size="6.5" letter-spacing="1.5" fill="var(--teal)"><textPath href="#ring">30 YEARS OF EXPERIENCE IN WELLNESS ·</textPath></text>
  </svg>
  <div class="abs label" style="left:602px;top:103px"><span class="rule"></span>About Us</div>
  <h2 class="abs title" style="left:602px;top:130px;font-size:40px">Our Story<br>At Vindmark</h2>
  <div class="abs" style="left:675px;top:276px;width:320px">
    <p>Our mission is simple: to empower individuals, both corporate and individual, to embrace a different perspective on health and wellness. Whether you're seeking to optimize your well-being or navigating life with a chronic illness, our holistic approach to wellness is designed to meet you where you are and help you thrive.</p>
    <p style="margin-top:16px">Discover the transformative power of personalized wellness with Della Quorne. Explore our services, meet our team, and take the first step towards a healthier, happier you.</p>
    <div class="signature" style="margin-top:12px">Dr Della P Quorne</div>
    <div style="font-size:8px;color:#999;margin-top:2px">DACM, L.Ac</div>
  </div>
</section>

<section class="quote" role="img" aria-label="Mountain lake landscape at dusk behind a quotation">
  <blockquote>"In meditation you try and let go of the past. You try to stop being anxious about the future. You focus on and enjoy the time you have now. When you are stressed and burdened by things, it is liberating to tune into the present, to enter into the deeper rhythm of your being." Aldous Pennick</blockquote>
  <svg class="abs" style="left:128px;top:228px" width="12" height="14" viewBox="0 0 12 14"><path d="M8 2 3 7l5 5" fill="none" stroke="#fff" stroke-width="2"/></svg>
  <svg class="abs" style="left:1056px;top:228px" width="12" height="14" viewBox="0 0 12 14"><path d="M4 2l5 5-5 5" fill="none" stroke="#fff" stroke-width="2"/></svg>
</section>

<section class="offerings">
  <div class="abs mountains" role="img" aria-label="Rugged mountain peaks glowing at sunset"></div>
  <div class="abs label" style="left:0;width:1200px;top:90px;justify-content:center"><span class="rule"></span>Offerings<span class="rule"></span></div>
  <h2 class="abs title" style="left:0;width:1200px;text-align:center;top:118px;font-size:38px">This Event Is For You!</h2>

  <article class="card" style="left:131px">
    <div class="img" style="background:linear-gradient(135deg,#c98a78,#e2c07a,#7aa0b8)" role="img" aria-label="Group of women in a fitness class with an instructor"></div>
    <div class="meta"><span>▭ 5/2/2024</span><span>·</span><span>◷ 5:00 PM</span></div>
    <p class="excerpt">Escape the hustle and bustle of daily life and immerse yourself in a weekend of relaxation and rejuvenation.</p>
    <div class="line"></div>
    <div class="more">READ MORE ›</div>
  </article>
  <article class="card" style="left:449px">
    <div class="img" style="background:linear-gradient(135deg,#8a8f80,#b0743e,#5c5a48)" role="img" aria-label="Two women jogging outdoors among autumn trees"></div>
    <div class="meta"><span>▭ 5/2/2024</span><span>·</span><span>◷ 5:00 PM</span></div>
    <p class="excerpt">Escape the hustle and bustle of daily life and immerse yourself in a weekend of relaxation and rejuvenation.</p>
    <div class="line"></div>
    <div class="more">READ MORE ›</div>
  </article>
  <article class="card" style="left:768px">
    <div class="img" style="background:linear-gradient(135deg,#b8c0b8,#6d8a5a,#3f5a3a)" role="img" aria-label="Group exercising together in a park"></div>
    <div class="meta"><span>▭ 5/2/2024</span><span>·</span><span>◷ 5:00 PM</span></div>
    <p class="excerpt">Escape the hustle and bustle of daily life and immerse yourself in a weekend of relaxation and rejuvenation.</p>
    <div class="line"></div>
    <div class="more">READ MORE ›</div>
  </article>
</section>

<section class="kind">
  <div class="abs label" style="left:222px;top:106px">Vindmark<span class="rule"></span></div>
  <h2 class="abs title" style="left:222px;top:132px;font-size:40px">Kind Words!</h2>
  <div class="abs" style="left:634px;top:132px;width:340px">
    <p>"I was provided an awesome experience at the spring retreat. The shared knowledge and experience blended beautifully. At the end of the weekend, I truly felt refreshed and renewed". Sela W</p>
    <p style="margin-top:12px">"When I first began seeing Dr. Della, I wasn't quite sure what to expect. I vividly remember her asking me about my goals, and my response was something like, 'I just want to feel like myself again. With each session, I experienced a reset and a profound sense of renewal Dr. Della explained that she was using Traditional East Asian Medicine to stimulate my body's natural healing processes. I was grappling with grief and depression, and Dr. Della's care has helped me in ways that words can't adequately express. Her guidance and treatment have been truly transformative. Rena L</p>
  </div>
</section>

<section class="reviews">
  <div class="abs strip"></div>
  <div class="abs label" style="left:222px;top:92px;color:#d8dfd2">Vindmark<span class="rule" style="background:#d8dfd2"></span></div>
  <h2 class="abs title" style="left:222px;top:120px;font-size:40px;color:var(--white)">Reviews</h2>
  <p class="abs" style="left:222px;top:188px;width:230px;font-size:10.5px;line-height:1.6;color:#e8ede4">Discover what others are saying about their transformative experiences with Della Quorne. Read reviews from our satisfied clients and join our community.</p>
  <div class="abs arrow-pair" style="left:222px;top:272px">
    <span class="dark" style="width:40px;height:40px"><svg width="10" height="10" viewBox="0 0 10 10"><path d="M6.5 1.5 3 5l3.5 3.5" fill="none" stroke="#fff" stroke-width="1.6"/></svg></span>
    <span class="soft" style="width:40px;height:40px"><svg width="10" height="10" viewBox="0 0 10 10"><path d="M3.5 1.5 7 5 3.5 8.5" fill="none" stroke="#fff" stroke-width="1.6"/></svg></span>
  </div>
  <article class="review" style="left:510px;top:74px;width:402px;height:262px">
    <div class="stars">★★★★★</div>
    <p class="text">Wir Waren Heute Bei Der Lieben Annika In Bergedorf Und Es War Wirklich Klasse. Wir Wurden Ausführlich Beraten &amp; Haben Uns Einfach Super Aufgehoben Gefühlt. Unsere Ringe Sind Bestellt Und Wir Freuen Uns, Wenn Wir Sie Abholen Dürfen!...</p>
    <div class="rule"></div>
    <div class="name">TOBIAS VERLAND</div>
    <svg class="abs" style="right:52px;bottom:26px" width="26" height="22" viewBox="0 0 26 22"><path d="M2 20c0-8 3-14 10-18l1 2c-4 3-5 6-5 8h4v8zM14 20c0-8 3-14 10-18l1 2c-4 3-5 6-5 8h4v8z" fill="#333"/></svg>
  </article>
  <article class="review" style="left:952px;top:96px;width:300px;height:224px">
    <div class="stars">★★★★★</div>
    <p class="text">Wir Waren Voll Und Ganz Zufrieden. Haben Uns Gut Aufgehoben Gefühlt. Super Liebe Betreuung. Wir Die Ringe Abgeholt Haben, Sehr Zu Empfehlen!</p>
    <div class="rule"></div>
    <div class="name">MIRA KESSEL</div>
  </article>
</section>

<section class="cta">
  <div class="abs label" style="left:0;width:1200px;top:97px;justify-content:center"><span class="rule"></span>Conatc Us<span class="rule"></span></div>
  <h2 class="abs title" style="left:0;width:1200px;top:122px;font-size:40px;line-height:1.22">Ready To Embark On<br>Your Journey To Personalized<br>Wellness?</h2>
  <p class="abs" style="left:350px;width:500px;top:292px;font-size:10px;line-height:1.6;color:var(--muted)">Take the first step towards a healthier, happier you. Contact us today to learn more or book your appointment!</p>
  <div class="btn-outline" style="left:513px;top:350px;width:175px;height:45px">Register Now</div>
</section>

<footer class="site-footer">
  <div class="abs footer-brand"><span class="dot"></span>Vindmark</div>
  <nav class="footer-nav">
    <a style="left:362px">Home</a>
    <a style="left:418px">About Us</a>
    <a style="left:498px">Services</a>
    <a style="left:573px">Individual Wellness</a>
    <a style="left:714px">Events &amp; Retreats</a>
    <a style="left:855px">Blog</a>
  </nav>
  <div class="social" aria-label="Social links">
    <span style="left:947px"></span><span style="left:977px"></span><span style="left:1007px"></span><span style="left:1038px"></span>
  </div>
  <div class="fine" style="left:132px">Copyright © 2024 Della Quorne</div>
  <div class="fine" style="left:929px">Privacy Policy</div>
  <div class="fine" style="left:1012px">Terms of Use</div>
</footer>

</body>
</html>
```